Brindle Assurance Information Security Company Site Facelift

Brindle Assurance needs a facelift to improve our online presence and attract new business. We provide information security services that include penetration testing, security research, training, and threat hunting. While we can provide these services to any organization, Brindle Assurance is a leader in the Industrial Control Systems (ICS) field and therefore need to be attractive to companies and individuals involved in factory, process, energy, and service sectors. We started with a simple website, but now we need your help to improve. Current website lives at: http://www.brindleassurance.example/We would like to update to a Hosted Wordpress site using the same logos.

Target Market(s)

Medium and large businesses. Specialty is anything with Industrial Control Systems (ICS) environments which are factories, manufacturing, energy.

Industry/Entity Type

Computer Security

Font styles to use
Sans Serif

Requirements
Must have
• Services - list of services
• Resources - list of software and training projects what will point to other sites such as Codewharf and Melkor Academy
• Blog - for company news and technical write-ups
• Contact page
• Team page
Nice to have
• Examples sites:
• Blue Ramparts: https://www.bluerampartsweb.example/
• Tallow Creek Information Security: https://www.bluerampartsweb.example/press/
• VelloGuard: https://www.velloguard.example/

```html
<!DOCTYPE html>
<html lang="en">
<head>
<meta charset="utf-8">
<title>Brindle Assurance</title>
<link href="https://fonts.googleapis.com/css2?family=Montserrat:wght@500;600;700&family=Poppins:wght@300;400;500;600&display=swap" rel="stylesheet">
<style>
:root{
  --orange:#f7931e;
  --red:#e8262b;
  --accent-grad:linear-gradient(90deg,#f7931e 0%,#ef5a24 60%,#e8262b 100%);
  --ink:#222222;
  --text:#555555;
  --muted:#7a7a7a;
  --soft:#f4f4f4;
  --dark:#232323;
  --white:#ffffff;
}
*{box-sizing:border-box;margin:0;padding:0}
html,body{width:1200px;height:3257px;overflow:hidden;background:var(--white)}
body{font-family:"Poppins",sans-serif;color:var(--text)}
.page{position:relative;width:1200px;height:3257px;overflow:hidden}

/* header */
.site-header{position:absolute;left:0;top:0;width:1200px;height:82px;background:var(--white);z-index:5}
.brand{position:absolute;left:124px;top:26px;display:flex;align-items:center;gap:8px;font-family:"Poppins",sans-serif;font-weight:600;font-size:13px;color:var(--red);text-transform:uppercase;letter-spacing:.2px}
.brand-dot{width:20px;height:20px;border-radius:50%;background:var(--red)}
.main-nav{position:absolute;right:123px;top:32px;display:flex;gap:44px;font-size:14px;color:#333}
.main-nav .is-active{color:var(--red)}

/* hero */
.hero-photo{position:absolute;left:0;top:82px;width:1200px;height:720px;background:radial-gradient(ellipse at 62% 35%,#3f5a5e 0%,#26353a 35%,#171c20 75%,#121416 100%)}
.hero-title{position:absolute;left:124px;top:262px;color:var(--white);font-family:"Montserrat",sans-serif;font-size:41px;line-height:50px;letter-spacing:.5px}
.hero-title .light{font-weight:500;display:block}
.hero-title .bold{font-weight:700;display:block}
.btn{display:inline-flex;align-items:center;justify-content:center;gap:9px;border-radius:22px;background:var(--accent-grad);color:var(--white);font-family:"Montserrat",sans-serif;font-weight:600;font-size:13px}
.btn svg{width:11px;height:8px}
.hero-cta{position:absolute;left:124px;top:398px;width:128px;height:41px}
.slider-arrow{position:absolute;top:330px;width:14px;height:22px}
.slider-arrow.prev{left:42px}.slider-arrow.next{right:42px}
.hero-curve{position:absolute;left:0;top:560px;width:1200px;height:340px}

/* service cards */
.service-card{position:absolute;top:618px;width:219px;height:257px;background:var(--white);border-radius:4px;box-shadow:0 2px 10px rgba(0,0,0,.1);text-align:center}
.service-icon{margin:32px auto 0;width:44px;height:44px;border-radius:50%;border:3px solid var(--red);position:relative}
.service-icon::after{content:"";position:absolute;inset:9px;border-radius:50%;border:2px solid var(--orange)}
.service-card h3{margin-top:24px;font-weight:500;font-size:16px;color:var(--ink);letter-spacing:.3px}
.service-card p{margin:12px auto 0;width:170px;font-size:12.5px;line-height:19px;color:var(--muted)}
.text-link{display:inline-flex;align-items:center;gap:7px;color:var(--orange);font-size:12.5px;font-weight:500}
.text-link svg{width:9px;height:7px}
.service-card .text-link{margin-top:18px}

/* section heading */
.section-title{position:absolute;font-family:"Montserrat",sans-serif;font-weight:700;font-size:26px}
.section-title.red{color:var(--red)}
.section-title.orange{color:var(--orange)}
.divider{position:absolute;width:111px;height:14px}

/* about */
.about-copy{position:absolute;left:124px;top:1043px;width:465px;font-size:14px;line-height:20.5px;letter-spacing:.2px}
.about-copy p{margin-bottom:10px}
.about-cta{position:absolute;left:123px;top:1290px;width:129px;height:42px}
.about-art{position:absolute;left:737px;top:974px;width:400px;height:398px;background:radial-gradient(closest-side at 42% 45%,#f46b26 0%,#ef4a26 55%,rgba(240,90,40,.25) 82%,rgba(255,255,255,0) 100%)}

/* resources */
.resources-band{position:absolute;left:0;top:1400px;width:1200px;height:650px}
.resource-card{position:absolute;top:1616px;width:300px;height:214px;background:var(--white);padding:4px;box-shadow:0 1px 6px rgba(0,0,0,.12)}
.resource-photo{position:relative;width:100%;height:100%;display:flex;flex-direction:column;justify-content:flex-end;align-items:center;text-align:center;color:var(--white);padding:0 10px 20px}
.resource-photo.monitors{background:linear-gradient(180deg,#5b6168 0%,#3a3d44 45%,#1b1b1f 100%)}
.resource-photo.phone{background:linear-gradient(180deg,#8a96a8 0%,#4a5568 50%,#1e2229 100%)}
.resource-photo.highlight{background:linear-gradient(135deg,rgba(247,147,30,.95) 0%,rgba(239,90,36,.92) 55%,rgba(232,38,43,.95) 100%);justify-content:center;padding:0 52px}
.resource-photo h4{font-family:"Montserrat",sans-serif;font-weight:700;font-size:15.5px;line-height:21px;letter-spacing:.3px;white-space:nowrap}
.resource-photo.highlight h4{font-family:"Poppins",sans-serif;font-weight:500;font-size:15px;margin-bottom:12px}
.resource-photo.highlight p{font-size:12.5px;line-height:19px}
.resource-photo.highlight .text-link{color:var(--white);margin-top:20px}
.view-all{position:absolute;left:541px;top:1899px;width:128px;height:42px;font-size:14px;gap:18px}

/* team */
.team-photo{position:absolute;left:124px;top:2228px;width:463px;height:429px;background:linear-gradient(120deg,#c9d2e4 0%,#7d8eb3 40%,#3b4a74 75%,#222a48 100%)}
.team-card{position:absolute;left:560px;top:2272px;width:515px;height:324px;background:var(--white);box-shadow:0 2px 14px rgba(0,0,0,.09);padding:28px 38px 0 40px}
.team-card h3{text-align:center;color:var(--orange);font-weight:400;font-size:16px}
.team-card .role{text-align:center;color:var(--ink);font-size:12.5px;margin-top:4px}
.team-card .bio{margin-top:24px;font-size:14px;line-height:20.5px;letter-spacing:.2px}
.team-card .bio p{margin-bottom:10px}
.team-more{position:absolute;left:755px;top:2580px;width:130px;height:30px;border-radius:16px;background:var(--white);box-shadow:0 2px 8px rgba(0,0,0,.1);display:flex;align-items:center;justify-content:center}

/* footer */
.footer-band{position:absolute;left:0;top:2730px;width:1200px;height:527px}
.footer-col{position:absolute;color:var(--white)}
.footer-col h5{font-weight:400;font-size:16px;letter-spacing:.3px}
.contact-col{left:124px;top:2925px}
.contact-col .call{margin-top:17px;font-size:18px}
.contact-col .call svg{width:14px;height:14px;vertical-align:-1px;margin:0 4px}
.contact-col .mail{font-size:13px;margin-top:2px}
.contact-col .org{margin-top:22px;font-size:14px}
.contact-col .addr{margin-top:8px;font-size:12.5px;line-height:21px}
.links-col{left:468px;top:2925px}
.links-col ul{list-style:none;margin-top:14px;font-size:13px;line-height:25.7px}
.news-col{left:693px;top:2925px}
.signup{margin-top:18px;display:flex;width:383px;height:42px}
.signup .field{flex:1;background:var(--white);color:#555;font-size:13px;display:flex;align-items:center;padding-left:17px}
.signup .go{width:93px;background:var(--accent-grad);display:flex;align-items:center;justify-content:center;font-family:"Montserrat",sans-serif;font-weight:600;font-size:13px}
.footer-rule{position:absolute;left:94px;top:3174px;width:1106px;height:1px;background:#3c3c3c}
.copyright{position:absolute;left:124px;top:3205px;color:var(--white);font-size:13.5px}
.copyright span{color:var(--orange)}
.socials{position:absolute;left:918px;top:3196px;display:flex;gap:9px}
.socials span{width:33px;height:33px;border-radius:50%;border:1px solid var(--orange)}
.socials span:first-child{background:var(--orange)}
</style>
</head>
<body>
<div class="page">

  <header class="site-header">
    <div class="brand"><span class="brand-dot"></span>Brindle Assurance</div>
    <nav class="main-nav">
      <span class="is-active">Home</span><span>Service</span><span>Reasourses</span><span>Blog</span><span>Team</span><span>Contact</span>
    </nav>
  </header>

  <div class="hero-photo" role="img" aria-label="Photo of hands typing on a laptop behind a glowing digital shield"></div>
  <h1 class="hero-title"><span class="light">OFFENSIVE SERVICES FROM</span><span class="bold">OFFENSIVE MINDS</span></h1>
  <a class="btn hero-cta">Contact Us <svg viewBox="0 0 11 8"><path d="M0 4h9M6 1l3 3-3 3" stroke="#fff" stroke-width="1.4" fill="none"/></svg></a>
  <svg class="slider-arrow prev" viewBox="0 0 14 22"><path d="M10 4 4 11l6 7" stroke="#fff" stroke-width="2.5" fill="none"/></svg>
  <svg class="slider-arrow next" viewBox="0 0 14 22"><path d="M4 4l6 7-6 7" stroke="#fff" stroke-width="2.5" fill="none"/></svg>

  <svg class="hero-curve" viewBox="0 0 1200 340" preserveAspectRatio="none">
    <defs><linearGradient id="heroBand" x1="0" x2="1"><stop offset="0" stop-color="#f7931e"/><stop offset=".6" stop-color="#ef5a24"/><stop offset="1" stop-color="#e8262b"/></linearGradient></defs>
    <path d="M0 26 Q560 210 1200 72 L1200 98 Q560 240 0 58 Z" fill="url(#heroBand)"/>
    <path d="M0 56 Q560 238 1200 96 L1200 340 L0 340 Z" fill="#fff"/>
  </svg>

  <article class="service-card" style="left:124px"><div class="service-icon"></div><h3>Aggressor</h3><p>It is a long establish factreader will be distract-edby the lorem ...</p><a class="text-link">Read More <svg viewBox="0 0 9 7"><path d="M0 3.5h7M5 1l2.5 2.5L5 6" stroke="currentColor" fill="none"/></svg></a></article>
  <article class="service-card" style="left:368px"><div class="service-icon"></div><h3>Defender</h3><p>It is a long establish factreader will be distract-edby the lorem ...</p><a class="text-link">Read More <svg viewBox="0 0 9 7"><path d="M0 3.5h7M5 1l2.5 2.5L5 6" stroke="currentColor" fill="none"/></svg></a></article>
  <article class="service-card" style="left:613px"><div class="service-icon"></div><h3>Instructor</h3><p>It is a long establish factreader will be distract-edby the lorem ...</p><a class="text-link">Read More <svg viewBox="0 0 9 7"><path d="M0 3.5h7M5 1l2.5 2.5L5 6" stroke="currentColor" fill="none"/></svg></a></article>
  <article class="service-card" style="left:857px"><div class="service-icon"></div><h3>Researcher</h3><p>It is a long establish factreader will be distract-edby the lorem ...</p><a class="text-link">Read More <svg viewBox="0 0 9 7"><path d="M0 3.5h7M5 1l2.5 2.5L5 6" stroke="currentColor" fill="none"/></svg></a></article>

  <h2 class="section-title red" style="left:124px;top:956px">About Us</h2>
  <svg class="divider" style="left:124px;top:1006px" viewBox="0 0 111 14"><path d="M0 7h46M65 7h46" stroke="#e8262b" stroke-width="1.5"/><circle cx="55.5" cy="7" r="6" fill="none" stroke="#ef5a24" stroke-width="2"/></svg>
  <div class="about-copy">
    <p>Brindle Assurance, a veteran owned company, is a team of sea-soned information security professionals who stand ready to assist you with your daily or emergency security efforts.</p>
    <p>We feel that security starts with a solid foundation of under-standing an organization's assets, people, and business require-ments.</p>
    <p>The financial, energy, media, and service industries to help ac-curately scope and complete your next security effort. Whether your team needs an architecture review.</p>
  </div>
  <a class="btn about-cta">Learn More <svg viewBox="0 0 11 8"><path d="M0 4h9M6 1l3 3-3 3" stroke="#fff" stroke-width="1.4" fill="none"/></svg></a>
  <div class="about-art" role="img" aria-label="Illustration of an orange isometric block cube topped by a security shield"></div>

  <svg class="resources-band" viewBox="0 0 1200 650" preserveAspectRatio="none">
    <defs><linearGradient id="band2" x1="0" x2="1"><stop offset="0" stop-color="#f7931e"/><stop offset=".6" stop-color="#ef5a24"/><stop offset="1" stop-color="#e8262b"/></linearGradient></defs>
    <path d="M0 70 Q700 -40 1200 98 L1200 560 Q640 660 0 540 Z" fill="#f4f4f4"/>
    <path d="M250 64 Q760 -30 1200 86 L1200 100 Q740 -10 250 64 Z" fill="url(#band2)"/>
    <path d="M0 538 Q660 660 1090 582 Q720 690 0 566 Z" fill="url(#band2)"/>
  </svg>
  <h2 class="section-title orange" style="left:531px;top:1510px">Resources</h2>
  <svg class="divider" style="left:544px;top:1556px" viewBox="0 0 111 14"><path d="M0 7h46M65 7h46" stroke="#e8262b" stroke-width="1.5"/><circle cx="55.5" cy="7" r="6" fill="none" stroke="#ef5a24" stroke-width="2"/></svg>

  <article class="resource-card" style="left:124px"><div class="resource-photo monitors" role="img" aria-label="Photo of a person at a desk facing security monitors"><h4>CEO Martin Osgood quoted in<br>Signal Weekly ransomware</h4></div></article>
  <article class="resource-card" style="left:451px"><div class="resource-photo highlight" role="img" aria-label="Photo of an office desk under an orange overlay"><h4>Instructor</h4><p>It is a long establish factreader will be distractedby the lorem ...</p><a class="text-link">Read More <svg viewBox="0 0 9 7"><path d="M0 3.5h7M5 1l2.5 2.5L5 6" stroke="currentColor" fill="none"/></svg></a></div></article>
  <article class="resource-card" style="left:776px"><div class="resource-photo phone" role="img" aria-label="Photo of hands holding a smartphone with a lock screen"><h4>Mobile Hacking: Using Tracehook<br>to Monitor Encryption</h4></div></article>
  <a class="btn view-all">View All <svg viewBox="0 0 11 8"><path d="M0 4h9M6 1l3 3-3 3" stroke="#fff" stroke-width="1.4" fill="none"/></svg></a>

  <h2 class="section-title orange" style="left:513px;top:2117px">Meet the Team</h2>
  <svg class="divider" style="left:556px;top:2163px" viewBox="0 0 111 14"><path d="M0 7h46M65 7h46" stroke="#e8262b" stroke-width="1.5"/><circle cx="55.5" cy="7" r="6" fill="none" stroke="#ef5a24" stroke-width="2"/></svg>
  <div class="team-photo" role="img" aria-label="Photo of the founder presenting on stage in an orange shirt"></div>
  <article class="team-card">
    <h3>Rowan T. Halvers</h3>
    <p class="role">Principal Consultant, Founder</p>
    <div class="bio">
      <p>Jack of All Trades. I have extensive experience in and inform ation technology penetration testing, web assessments, wireless assessments, architecture review, incident respon-se/digital forensics.</p>
      <p>For the past three years I have leveraged these skills to assist Larkspur Studios.</p>
      <p>as a Senior Manager, Incident Response (IR) and, for an eight-month period, &nbsp;Management (RVM).</p>
    </div>
  </article>
  <a class="team-more"><span class="text-link">Read More <svg viewBox="0 0 9 7"><path d="M0 3.5h7M5 1l2.5 2.5L5 6" stroke="currentColor" fill="none"/></svg></span></a>

  <svg class="footer-band" viewBox="0 0 1200 527" preserveAspectRatio="none">
    <defs><linearGradient id="band3" x1="0" x2="1"><stop offset="0" stop-color="#f7931e"/><stop offset=".6" stop-color="#ef5a24"/><stop offset="1" stop-color="#e8262b"/></linearGradient></defs>
    <path d="M0 146 Q560 -60 1200 70 L1200 527 L0 527 Z" fill="#232323"/>
    <path d="M260 80 Q700 -30 1200 42 L1200 72 Q720 -10 260 80 Z" fill="url(#band3)"/>
  </svg>
  <div class="footer-col contact-col">
    <h5>Contact Us</h5>
    <p class="call">Call Us:<svg viewBox="0 0 14 14"><path d="M3 1l2 3-1.3 1.3a8 8 0 0 0 5 5L10 9l3 2-1 2.5C6 13 1 8 .5 2z" fill="#fff"/></svg>555-014-2290</p>
    <p class="mail">e. hello@brindleassurance.example</p>
    <p class="org">Brindle Assurance</p>
    <p class="addr">4120 Quarry Bend Road, Suite 210<br>Lorem, Ipsum 40918</p>
  </div>
  <div class="footer-col links-col">
    <h5>Quick Links</h5>
    <ul><li>Home</li><li>Service</li><li>Resources</li><li>Blog</li><li>Team</li><li>Contact</li></ul>
  </div>
  <div class="footer-col news-col">
    <h5>Subscribe for Newsletter</h5>
    <div class="signup"><span class="field">Enter Your Email</span><span class="go">Sign Up</span></div>
  </div>
  <div class="footer-rule"></div>
  <p class="copyright">© 2019 <span>Brindle Assurance.</span> All Right Reserved</p>
  <div class="socials" aria-label="Social links"><span></span><span></span><span></span><span></span></div>

</div>
</body>
</html>
```